Digital Menu Board for Restaurant

I want a digital menu board for our new restaurant. I have provided the sample of what I kind of want.
This is to be on a 55 inch tv so it needs to be the correct aspect ratio of 4:5

Font styles to use
Serif
Sans Serif

Colors
f59296
f04a50
ec1f27
ffffff
fffef7
fbed22
ffc214
0592cd
e5519f

Requirements
Must have
• fun, maybe something moving? bright colors on a darker background so it's easy to read or dark font on a light background.

```html
<!DOCTYPE html>
<html lang="en">
<head>
<meta charset="utf-8">
<title>Salt Tide Menu Board</title>
<link rel="stylesheet" href="https://fonts.googleapis.com/css2?family=Oswald:wght@400;500&family=Kaushan+Script&display=swap">
<style>
:root{
  --page:#e9e9e9;
  --night:#2b1530;
  --cream:#fffef7;
  --sun:#ffc214;
  --lemon:#fbed22;
  --coral:#f04a50;
  --flame:#f26b3a;
  --rose:#f59296;
  --teal:#0f4a55;
}
*{margin:0;padding:0;box-sizing:border-box}
html,body{width:1200px;height:900px;overflow:hidden;background:var(--page)}
.board{position:absolute;left:0;top:112px;width:1200px;height:675px;background:var(--night);overflow:hidden;font-family:"Oswald",sans-serif}
.scene{position:absolute;left:0;top:0;width:1200px;height:330px}
.frame{position:absolute;left:22px;top:14px;right:22px;bottom:24px;border:3px solid var(--cream);pointer-events:none}
.brand{position:absolute;left:505px;top:188px;font-family:"Oswald",sans-serif;font-weight:500;font-size:44px;line-height:1.2;color:var(--coral);letter-spacing:1px;white-space:nowrap}
.section-title{position:absolute;font-family:"Kaushan Script",cursive;font-size:30px;color:var(--lemon);line-height:1;white-space:nowrap}
.section-title.coral{color:var(--flame)}
.section-title.kids{font-size:22px;top:314px}
.section-title small{font-size:12px}
.item{position:absolute;width:200px}
.item h3{font-weight:400;font-size:17.5px;color:var(--flame);line-height:1.2;white-space:nowrap}
.item p{margin-top:5px;font-size:11px;line-height:15.5px;color:var(--sun)}
.list{position:absolute;list-style:none;font-size:14.5px;line-height:19px;color:var(--sun);letter-spacing:-.2px}
.list.wide{width:260px}
.divider{position:absolute;top:313px;width:2px;height:332px;background:var(--cream)}
</style>
</head>
<body>
<main class="board">
  <svg class="scene" role="img" aria-label="Sunset beach illustration with palm trees, umbrella and deck chair" viewBox="0 0 1200 330" preserveAspectRatio="none">
    <defs>
      <linearGradient id="sky" x1="0" y1="0" x2="0" y2="1">
        <stop offset="0" stop-color="#f7a531"/>
        <stop offset="0.55" stop-color="#ffc214"/>
        <stop offset="1" stop-color="#f59296"/>
      </linearGradient>
    </defs>
    <rect width="1200" height="330" fill="url(#sky)"/>
    <path d="M0 280 C150 300 320 300 480 230 C620 170 760 110 900 60 L1200 40 L1200 330 L0 330 Z" fill="var(--night)"/>
    <path d="M880 90 C960 60 1100 70 1200 80 L1200 260 C1100 250 980 240 900 220 Z" fill="var(--teal)" opacity="0.55"/>
  </svg>
  <div class="frame"></div>

  <div class="brand">Salt Tide</div>

  <h2 class="section-title" style="left:55px;top:308px">Between Buns</h2>
  <h2 class="section-title" style="left:474px;top:308px">Green Shore</h2>
  <h2 class="section-title coral kids" style="left:678px">Seashell Finders <small>(kids)</small></h2>
  <h2 class="section-title coral" style="left:892px;top:308px">Shakes</h2>
  <h2 class="section-title coral" style="left:678px;top:505px">Drinks</h2>
  <h2 class="section-title coral" style="left:892px;top:505px">Sides</h2>

  <div class="divider" style="left:449px"></div>
  <div class="divider" style="left:661px"></div>

  <article class="item" style="left:55px;top:356px;width:172px">
    <h3>1st Point Pulled Pork</h3>
    <p>Pulled Pork, Marlo's Sassy BBQ Sauce, Chopped Bacon, Pepperjack Cheese, and Fried Jalapeno Peppers on a Ciabatta Bun</p>
  </article>
  <article class="item" style="left:55px;top:452px;width:172px">
    <h3>2nd Point Pulled Pork</h3>
    <p>Pulled Pork, Marlo's Sweet Raspberry BBQ Sauce, and Coleslaw on a Ciabatta Bun</p>
  </article>
  <article class="item" style="left:55px;top:537px;width:380px">
    <h3>Spiniker Point Burger</h3>
    <p>Two Smokehouse 1/2 Pound Burger, Crumbled Bacon, Marlo's Sassy BBQ Sauce, Cheese, and Onion Rings on a Toasted Brioche Bun</p>
  </article>
  <article class="item" style="left:257px;top:355px;width:185px">
    <h3>The Rock Burger</h3>
    <p>Two Smokehouse 1/2 Pound Patties, Cheese, Lettuce, Tomato, Onion, Pickles On Toasted Brioche Bun</p>
  </article>
  <article class="item" style="left:257px;top:436px;width:180px">
    <h3>Rainbow Cove Sandwich</h3>
    <p>Chicken Salad - Smoke Chicken, Celery and Onion Mixed with our BBQ Mayo and Topped with Seasoned Tomato on a Hoagie Roll.</p>
  </article>

  <article class="item" style="left:474px;top:356px;width:180px">
    <h3>Rainbow Cove Sandwich</h3>
    <p>Pulled Pork And Black Beans On A Bed Of Romaine, Tomato And Onion With Sweet and Sour Raspberry Pineapple Sauce.</p>
  </article>
  <article class="item" style="left:474px;top:453px;width:180px">
    <h3>West Side Salad</h3>
    <p>BBQ Pulled Pork, Crumbled Bacon, Candied Walnuts, Feta Cheese, Red Onion, Spinach and Lettuce with Ranch Dressing or Raspberry Vinaigrette</p>
  </article>
  <article class="item" style="left:474px;top:551px;width:180px">
    <h3>East Side Salad</h3>
    <p>Spinach and Lettuce, Chopped Apples, Candied Walnuts, Onion, Feta Cheese with Marlo's Raspberry Vinaigrette Add Chicken</p>
  </article>

  <ul class="list" style="left:678px;top:355px">
    <li>Little Cheeseburger</li>
    <li>Pulled pork sandwich</li>
    <li>Mini Corn Dogs</li>
    <li>Chicken salad sandwich</li>
    <li>Fries/Onion Rings</li>
  </ul>
  <ul class="list" style="left:678px;top:545px;width:190px">
    <li>Fizzo, Diet Fizzo, Kolo, Diet Kolo, Peak Citrus, Diet Citrus, Lemonade, Lemon-Lime Pop, Dr Spice</li>
  </ul>
  <ul class="list wide" style="left:892px;top:355px">
    <li>Marlo's Signature Raspberry Jammin Shake</li>
    <li>Raspberry Cookie Crumble Shake</li>
    <li>Raspberry Hazelnut Cocoa Bomb Shake</li>
    <li>Raspberry Beachin' Shake (Pina Colada)</li>
    <li>Raspberry Brownie Shake</li>
    <li>Caramel Shake</li>
    <li>Chocolate Shake</li>
  </ul>
  <ul class="list" style="left:892px;top:548px">
    <li>Seasoned Fries</li>
    <li>Onion Rings</li>
    <li>Sweet Cornbread</li>
  </ul>
  <ul class="list" style="left:1009px;top:548px">
    <li>Sweet Coleslaw</li>
    <li>Macaroni Salad</li>
    <li>Side Salad</li>
  </ul>
</main>
</body>
</html>
```